Wine Shop Banners

Banner graphic/images required
Require banner images to match the present online wine shop.

www.kelterhaus-traube.de

The wine-shop presently has a very clean, simple design, lots of white space, which is very much the trend at the moment.

Requirements
Images or graphic design for present banners visible on the homepage

The colour and feeling of the banners must fit in with the present clean, simple design.

Work required
3 large slide-card/banners (can be more) and 3 smaller fixed banners below. Please view website to see present position of banners.

LARGE BANNERS x 3

Something special with white background within the banner space
White background on each slide-card. Small individual graphic image in the middle of the slide card. This could be either a simple element of wine:
ingredients, fruit (grape), bottle, cork, old bottle label etc. just displaying one item on each slide-card. Preferably with high quality graphic features.

Note:
We are trying the steer away from the classic stereotype wineshop design. The image/s should have a higher, individual graphic touch, which gives the design something different. Sometimes such artistic work is displayed in steampunk or even in nostalgic design, which leaves the viewer slightly memorized with the content.
To clarify: we are not looking for a full steampunk design but possibly certain elements of this will give you an idea what we mean. That is to say, the design can go slightly in this direction without going over the top. Something small but very eye-catching.

SMALLER BANNERS x 3

One idea is:
Showing a symbol e.g. - discount sign "%" against a white background but again with a high graphic quality.

Target Market(s)

People interested in purchasing wine.
Ages approx. 25 to 65

Industry/Entity Type

Shop

Requirements
Must have
• Something special with white background
• Small individual graphic image in the middle of the slide card.
Nice to have
• The image/s should have a higher, individual graphic touch, which gives the design something different. Something that leaves the viewer slightly memorized with the content.
Should not have
• Not the typical classical design that is often seen on wine shops.

```html
<!DOCTYPE html>
<html lang="de">
<head>
<meta charset="utf-8">
<title>Kelterhaus Traube – Wein Shop</title>
<link rel="stylesheet" href="https://fonts.googleapis.com/css2?family=Open+Sans:wght@400;600&family=Cinzel:wght@400;500&family=Lora:wght@400;600&display=swap">
<style>
:root{
  --ink:#444;
  --muted:#8a8a8a;
  --olive:#4d5a2c;
  --wine:#a8173d;
  --lime:#c5cf52;
  --lime-bar:#cfd95e;
  --price:#b4bb2a;
  --line:#d9d9d9;
  --panel:#f6f6f4;
}
*{box-sizing:border-box;margin:0;padding:0}
html,body{width:1200px;height:675px;overflow:hidden;background:#fff}
body{position:relative;font-family:"Open Sans",sans-serif;color:var(--ink)}
.abs{position:absolute}

.brand{left:252px;top:8px;width:120px;text-align:left}
.brand-name{font-family:"Cinzel",serif;font-size:23px;font-weight:500;color:var(--olive);letter-spacing:1px;line-height:34px}
.brand-tag{font-family:"Cinzel",serif;font-size:23px;font-weight:500;color:var(--olive);letter-spacing:1px;line-height:22px}

.search{left:601px;top:23px;width:197px;height:23px;border:1px solid #555;display:flex}
.search-field{flex:1;display:flex;align-items:center;gap:8px;padding-left:7px;font-size:10px;color:#666}
.search-go{width:28px;background:var(--wine);color:#fff;font-size:10px;font-weight:600;display:flex;align-items:center;justify-content:center}

.nav{top:77px;left:262px;display:flex;font-size:12px;color:#555}
.nav span{position:absolute;white-space:nowrap}
.account{left:844px;top:73px;display:flex;align-items:center;gap:6px;font-size:10px;color:#555}

.sidebar{left:252px;top:104px;width:145px}
.filter-bar{height:24px;background:var(--lime-bar);font-size:10px;font-weight:600;color:#4a4a2a;padding-left:7px;line-height:24px}
.filter-title{position:absolute;left:1px;font-size:11.5px;color:var(--lime);text-transform:uppercase}
.filter-list{position:absolute;left:0;list-style:none;font-size:10px;color:#444}
.filter-list li{height:15.2px;line-height:15.2px;white-space:nowrap}
.filter-list li::before{content:"›";margin-right:5px;color:#555}
.filter-list .n{color:var(--muted)}
.scrollbar{position:absolute;left:129px;width:13px;background:#f1f1f1}
.scrollbar .thumb{position:absolute;left:1px;width:11px;background:#c1c1c1}
.clip{position:absolute;left:0;overflow:hidden}

.price-range{position:absolute;left:4px;top:422px;width:130px}
.price-track{height:3px;background:#ddd;border:1px solid #bbb;margin-top:4px}
.price-knob{position:absolute;top:0;width:7px;height:10px;border:1px solid #999;border-radius:3px;background:#fff}
.price-label{position:absolute;top:12px;width:100%;text-align:center;font-size:9px;color:#444}
.region-input{position:absolute;left:1px;top:479px;width:143px;height:27px;border:1px solid #ccc;font-size:9px;color:#888;padding-left:8px;line-height:25px}

.hero{left:405px;top:105px;width:543px;height:210px;border:1px solid #dcdcdc;background:linear-gradient(180deg,#fafaf8,#f1f1ee)}
.hero-kicker{position:absolute;left:31px;top:55px;font-family:"Cinzel",serif;font-size:10.5px;color:var(--wine)}
.hero-title{position:absolute;left:30px;top:67px;font-family:"Cinzel",serif;font-size:31px;line-height:32px;color:var(--olive);letter-spacing:.5px}
.hero-sub{position:absolute;left:32px;top:139px;font-family:"Lora",serif;font-size:9px;color:#444}
.hero-art{position:absolute;left:286px;top:42px;width:232px;height:150px;border-radius:50% 40% 45% 50%;background:radial-gradient(circle at 40% 50%,#2a2d45 0,#3a3d5c 40%,#6f8a3a 70%,rgba(240,240,236,0) 72%)}

.promo{top:324px;width:176px;height:82px;border:1px solid #dcdcdc;background:linear-gradient(180deg,#fbfbfa,#f0f0ed);text-align:center}
.promo-title{font-family:"Cinzel",serif;color:var(--olive);font-size:19px;letter-spacing:.5px}
.promo-small{font-family:"Cinzel",serif;color:var(--wine);font-size:6.5px}
.promo-accent{font-family:"Cinzel",serif;color:var(--wine)}
.promo-ornament{position:absolute;left:14px;top:0;width:146px;height:22px;background:linear-gradient(180deg,#d8d8d2,rgba(240,240,237,0))}

.featured{left:404px;top:420px;width:546px}
.featured-head{display:flex;align-items:center;gap:6px;font-family:"Lora",serif;font-weight:600;font-size:11.5px;color:#333}
.featured-rule{position:absolute;top:19px;left:0;width:546px;height:3px;background:#eee}
.pager{position:absolute;right:0;top:0;display:flex;gap:2px}
.pager span{width:13px;height:14px;border:1px solid #777;display:flex;align-items:center;justify-content:center}

.product{top:444px;width:135px;height:231px;background:var(--panel);text-align:center}
.bottle{position:absolute;top:10px;left:50%;transform:translateX(-50%);width:30px;height:124px;border-radius:10px 10px 6px 6px}
.product-name{position:absolute;top:144px;left:4px;right:4px;font-size:9.5px;line-height:11px;color:#555}
.product-price{position:absolute;top:184px;width:100%;font-size:16px;font-weight:600;color:var(--price)}
.product-price sup{font-size:7px;color:#555}
.product-unit{position:absolute;top:212px;width:100%;font-size:9px;color:#555}
</style>
</head>
<body>

<div class="abs brand">
  <div class="brand-name">KELTERHAUS</div>
  <div class="brand-tag">TRAUBE</div>
</div>

<div class="abs search">
  <div class="search-field">
    <svg width="9" height="9" viewBox="0 0 10 10"><circle cx="4" cy="4" r="3" fill="none" stroke="#a8173d" stroke-width="1.6"/><line x1="6.3" y1="6.3" x2="9" y2="9" stroke="#a8173d" stroke-width="1.6"/></svg>
    Suche
  </div>
  <div class="search-go">GO</div>
</div>

<nav class="abs nav">
  <span style="left:0">Rotwein</span>
  <span style="left:68px">Weißwein</span>
  <span style="left:145px">Rosewein</span>
  <span style="left:220px">Sekt / Champagner</span>
  <span style="left:347px">Sonderangebote</span>
  <span style="left:460px">Probierpakete</span>
</nav>

<div class="abs account">
  <svg width="16" height="18" viewBox="0 0 16 18"><circle cx="8" cy="5" r="3.8" fill="none" stroke="#555" stroke-width="1.3"/><path d="M1.5 17v-3.5a3 3 0 0 1 3-3h7a3 3 0 0 1 3 3V17z" fill="none" stroke="#555" stroke-width="1.3"/></svg>
  <svg width="20" height="17" viewBox="0 0 20 17" style="margin-left:4px"><path d="M1 2h3l2 9h10l2-7H5" fill="none" stroke="#555" stroke-width="1.3"/><circle cx="8" cy="14.5" r="1.4" fill="#555"/><circle cx="15" cy="14.5" r="1.4" fill="#555"/></svg>
  <span>(0)</span>
  <svg width="18" height="16" viewBox="0 0 18 16" style="margin-left:6px"><path d="M9 15 2.2 8.2A4 4 0 0 1 9 2.6a4 4 0 0 1 6.8 5.6z" fill="none" stroke="#555" stroke-width="1.3"/></svg>
  <span>(0)</span>
</div>

<aside class="abs sidebar">
  <div class="filter-bar">DETAILSUCHE</div>

  <div class="filter-title" style="top:32px">Land</div>
  <div class="clip" style="top:54px;width:128px;height:114px">
    <ul class="filter-list" style="top:0">
      <li>Italien <span class="n">(89)</span></li>
      <li>Frankreich <span class="n">(74)</span></li>
      <li>Deutschland <span class="n">(61)</span></li>
      <li>Spanien <span class="n">(35)</span></li>
      <li>Südafrika <span class="n">(15)</span></li>
      <li>Australien <span class="n">(12)</span></li>
      <li>Österreich <span class="n">(11)</span></li>
      <li>Portugal <span class="n">(10)</span></li>
    </ul>
  </div>
  <div class="scrollbar" style="top:54px;height:114px">
    <svg class="abs" style="left:3px;top:3px" width="7" height="5"><path d="M0 5 3.5 0 7 5z" fill="#777"/></svg>
    <div class="thumb" style="top:15px;height:45px"></div>
    <svg class="abs" style="left:3px;top:105px" width="7" height="5"><path d="M0 0h7L3.5 5z" fill="#333"/></svg>
  </div>

  <div class="filter-title" style="top:180px">Geschmack</div>
  <ul class="filter-list" style="top:201px">
    <li>Trocken <span class="n">(307)</span></li>
    <li>Halbtrocken <span class="n">(9)</span></li>
    <li>Lieblich <span class="n">(5)</span></li>
    <li>Süß <span class="n">(2)</span></li>
    <li>Edelsüss <span class="n">(1)</span></li>
  </ul>

  <div class="filter-title" style="top:290px">Farbe</div>
  <ul class="filter-list" style="top:311px">
    <li>Rot <span class="n">(157)</span></li>
    <li>Weiß <span class="n">(129)</span></li>
    <li>Prickelnd <span class="n">(22)</span></li>
    <li>Rosé <span class="n">(13)</span></li>
    <li>Champagner <span class="n">(9)</span></li>
  </ul>

  <div class="filter-title" style="top:398px">Preis</div>
  <div class="price-range">
    <div class="price-track"></div>
    <div class="price-knob" style="left:0"></div>
    <div class="price-knob" style="left:125px"></div>
    <div class="price-label">2 € - 75 €</div>
  </div>

  <div class="filter-title" style="top:452px">Region</div>
  <div class="region-input">Region suchen ...</div>
  <div class="clip" style="top:517px;width:128px;height:54px">
    <ul class="filter-list" style="top:0">
      <li>Abruzzen <span class="n">(4)</span></li>
      <li>Alentejo <span class="n">(2)</span></li>
      <li>Apulien <span class="n">(10)</span></li>
      <li>Baden <span class="n">(4)</span></li>
    </ul>
  </div>
  <div class="scrollbar" style="top:517px;height:54px">
    <svg class="abs" style="left:3px;top:3px" width="7" height="5"><path d="M0 5 3.5 0 7 5z" fill="#777"/></svg>
    <div class="thumb" style="top:13px;height:15px"></div>
  </div>
</aside>

<section class="abs hero">
  <div class="hero-kicker">LOREM IPSUM DOLOR SIT AMET, CONSECTETUR</div>
  <div class="hero-title">REAL ORGANIC<br>GRAPES</div>
  <div class="hero-sub">Surprise of &nbsp;Wine Gifts for Someone Special</div>
  <div class="hero-art" role="img" aria-label="Bunch of dark grapes with vine leaves beside a cork and corkscrew"></div>
</section>

<div class="abs promo" style="left:405px">
  <div class="promo-title" style="margin-top:18px">FREE SHIPPING</div>
  <div class="promo-small">ON ORDERS OVER</div>
  <div class="promo-accent" style="font-size:19px;line-height:22px">$25</div>
</div>
<div class="abs promo" style="left:588px">
  <div class="promo-ornament" role="img" aria-label="Engraved grape cluster border"></div>
  <div class="promo-title" style="margin-top:28px">CELEBRATE</div>
  <div class="promo-small">YOUR ANNIVERSARY WITH TASTE</div>
</div>
<div class="abs promo" style="left:772px">
  <div class="promo-title" style="margin-top:18px">SPECIAL OFFER</div>
  <div class="promo-accent" style="font-size:30px;line-height:30px">20%</div>
</div>

<section class="abs featured">
  <div class="featured-head">
    <svg width="12" height="12" viewBox="0 0 12 12"><circle cx="6" cy="6" r="5" fill="none" stroke="#a8173d" stroke-width="1.2"/><path d="M5 3.5 7.5 6 5 8.5" fill="none" stroke="#a8173d" stroke-width="1.2"/></svg>
    Ausgewählte Produkte
  </div>
  <div class="pager">
    <span><svg width="5" height="8"><path d="M4 0 0 4l4 4" fill="none" stroke="#555"/></svg></span>
    <span><svg width="5" height="8"><path d="M1 0l4 4-4 4" fill="none" stroke="#555"/></svg></span>
  </div>
  <div class="featured-rule"></div>
</section>

<article class="abs product" style="left:402px">
  <div class="bottle" role="img" aria-label="Bottle of rosé sparkling wine" style="background:linear-gradient(180deg,#e8c9c4,#e7a9a6 60%,#d9858a)"></div>
  <div class="product-name">Pinot Rosé, Le Colline, Spumante Brut</div>
  <div class="product-price">9,80 €<sup>*</sup></div>
  <div class="product-unit">13,07 € per Liter</div>
</article>
<article class="abs product" style="left:540px">
  <div class="bottle" role="img" aria-label="Bottle of white wine" style="background:linear-gradient(180deg,#e6e6e0,#8f8a54 30%,#4d4a2c)"></div>
  <div class="product-name">Bianco del Lago, Villa Serena</div>
  <div class="product-price">11,95 €<sup>*</sup></div>
  <div class="product-unit">15,93 € per Liter</div>
</article>
<article class="abs product" style="left:678px">
  <div class="bottle" role="img" aria-label="Bottle of red wine" style="background:linear-gradient(180deg,#2a1418,#1c1012 60%,#2b1a1c)"></div>
  <div class="product-name">Brouilly, AP, Château des Collines</div>
  <div class="product-price">11,95 €<sup>*</sup></div>
  <div class="product-unit">15,93 € per Liter</div>
</article>
<article class="abs product" style="left:816px">
  <div class="bottle" role="img" aria-label="Bottle of Marsala dessert wine" style="background:linear-gradient(180deg,#3a2a18,#9c6a2e 35%,#c79a55)"></div>
  <div class="product-name">Marsala Superiore Secco, Casa Marino</div>
  <div class="product-price">14,80 €<sup>*</sup></div>
  <div class="product-unit">19,73 € per Liter</div>
</article>

</body>
</html>
```